New Vidora Channel Banner Graphic/Logo for "Cozy Nook Attic Sound"

Create a banner for my new Vidora channel for Cozy Nook Attic Sound. This is partially a logo project, but the logo will not be used elsewhere. Check out Vidora channels to see the banners others have created. This channel is about my home studio, the gear, microphones, musical instruments, wiring, software etc. that goes into a home studio. It's a free channel, made for sharing information. This is a graphic design that will be posted on vidora using built-in vidora tools.
Updates

More information about this project! I'm staring a channel called "Cozy Nook Attic Sound" on vidorastream.net. I need a deign for this banner and a logo for Cozy Nook Attic Sound. I called the channel by that name because my music studio is my happy place. It's about music and instruments (gutars, piano, drums, percussion) singing (microhpones), creativity, and what you'd expect form musicians. It's also about technology, recording, live-streaming, music videos, etc. It is my hobby, not my profession. I will be creating content for other amateur home studio aficionados and hobbyists. There are a lot of home studio channels and videos you can look at on vidora to get a flavor for musicians and studios. Usually fairly tech-heavy. An appeal of my channel will be a very approachable, "i'm the same as you" welcome for people that are doing it to enjoy it.

I put this project in the wrong category to start. This has been fixed, but I think benefits I would have received (such as invited designers) and announcement of project in the correct category mean I'm not getting designers. Your initial menu should be improved. I'm having a banner created for a web page in Vidora. I think it is easy to mistake that for a web design when it is really a graphic design for the web.

Target Market(s)

Similar to myself, people as interested in studio/production tech as they are in making music, perhaps trending a bit older and successful enough to afford some gear!

Number of Pages Required

1 page

Font styles to use
Sans Serif

Requirements
Must have
• This is not really a web design, i may have miscategorized. Please see uploaded docs for pics of similar banner on a Vidora page. ADDED 1/5: As this is a vidora channel that could be viewed on any device, the banner should be friendly in this way and design or design variations needed for PC, Tabrix, phone vie3wing.

Here are the Vidora size specs:
Banner image guidelines
Your banner image must meet the following criteria:

Minimum dimension for upload: 2048 x 1152 px with an aspect ratio of 16:9.
At the Minimum dimension, the safe area for text and logos: 1235 x 338 px. Larger images may get cropped on certain views or devices.
File size: 6 MB or smaller.
How to resize images

You can use your computer's image editor or an online image resizer to resize the images. For example, you can use Preview on an Quince computer or Microsoft Photos on Windows.

```html
<!DOCTYPE html>
<html lang="en">
<head>
<meta charset="utf-8">
<title>Cozy Nook Attic Sound — Channel Identity</title>
<link href="https://fonts.googleapis.com/css2?family=Poppins:wght@400;500;600;700&family=Montserrat:wght@900&family=Roboto:wght@400;500&display=swap" rel="stylesheet">
<style>
  :root {
    --brand-red: #ef4255;
    --ink: #111111;
    --paper: #ffffff;
    --light-panel: #f7f7f7;
    --dark-panel: #1c1c1c;
    --bar-dark: #2a2a2a;
    --bar-darker: #232323;
    --muted: #9a9a9a;
    --subscribe: #e62117;
  }
  * { margin: 0; padding: 0; box-sizing: border-box; }
  html, body { width: 782px; height: 1200px; overflow: hidden; background: var(--paper); }
  body { position: relative; font-family: "Poppins", sans-serif; color: var(--ink); }
  .abs { position: absolute; }

  .section-title {
    position: absolute; left: 0; width: 782px; text-align: center; z-index: 2;
    font-size: 12.5px; font-weight: 500; letter-spacing: 1px; color: var(--ink);
  }
  .section-title .underline { position: relative; }
  .section-title .underline::after {
    content: ""; position: absolute; left: 0; right: 0; bottom: -4px; height: 2.5px; background: var(--brand-red);
  }
  .section-title--on-light { clip-path: inset(0 391px 0 0); }
  .section-title--on-dark { clip-path: inset(0 0 0 391px); color: #ffffff; }

  /* Logo presentation */
  .logo-light { left: 0; top: 0; width: 391px; height: 261px; background: var(--light-panel); }
  .logo-dark { left: 391px; top: 0; width: 391px; height: 261px; background: var(--dark-panel); }
  .wordmark {
    position: absolute; font-family: "Poppins", sans-serif; font-weight: 500;
    text-transform: uppercase; line-height: 1.05; letter-spacing: .5px;
    display: flex; align-items: center; gap: 8px;
  }
  .wordmark .dot { width: 8px; height: 8px; border-radius: 50%; background: currentColor; flex: none; }
  .wordmark--lg { font-size: 19px; width: 260px; }
  .wordmark--md { font-size: 12px; width: 150px; gap: 6px; }
  .wordmark--md .dot { width: 7px; height: 7px; }
  .wordmark--red { color: var(--brand-red); }
  .wordmark--white { color: #ffffff; }

  /* Banner */
  .banner { left: 0; top: 298px; width: 782px; height: 441px; overflow: hidden;
    background:
      radial-gradient(ellipse 120px 90px at 390px 40px, rgba(170,170,170,.35), rgba(170,170,170,0) 100%),
      radial-gradient(ellipse 60px 50px at 570px 175px, rgba(150,150,150,.35), rgba(150,150,150,0) 100%),
      radial-gradient(ellipse 50px 45px at 625px 175px, rgba(150,150,150,.3), rgba(150,150,150,0) 100%),
      linear-gradient(180deg, rgba(255,255,255,0) 0%, rgba(255,255,255,0) 55%, rgba(185,185,185,.35) 62%, rgba(215,215,215,.2) 75%, rgba(230,230,230,0) 100%),
      linear-gradient(90deg, #e9e9e9 0%, #ececec 40%, #e3e3e3 75%, #d6d6d6 100%); }
  .banner-pattern { position: absolute; left: -140px; top: -40px; width: 410px; height: 520px; border-radius: 50%;
    background:
      radial-gradient(circle at 75% 35%, rgba(190,150,200,.55), rgba(190,150,200,0) 30%),
      radial-gradient(circle at 80% 70%, rgba(190,130,90,.45), rgba(190,130,90,0) 28%),
      radial-gradient(circle at 40% 50%, #3c3c48 0%, #5e5464 45%, #a693a9 80%, #d9cfd9 100%);
    opacity: .88; }
  .tagline { position: absolute; font-family: "Poppins", sans-serif; }
  .tagline h2 { font-size: 11px; font-weight: 600; line-height: 1.2; color: #2a2a2a; text-transform: uppercase; }
  .tagline p { font-size: 5.6px; color: #444; margin-top: 5px; }
  .contact { position: absolute; display: flex; align-items: center; gap: 4px; font-size: 5.6px; color: #444; }
  .contact .icon { width: 9px; height: 9px; border-radius: 50%; background: var(--brand-red); display: flex; align-items: center; justify-content: center; }

  /* Channel preview */
  .topbar { left: 0; top: 778px; width: 782px; height: 23px; background: var(--bar-darker); }
  .search { position: absolute; left: 214px; top: 7px; width: 206px; height: 10px; background: #121212; }
  .search-btn { position: absolute; left: 420px; top: 7px; width: 27px; height: 10px; background: #333; }
  .site-name { position: absolute; left: 143px; top: 5px; font-family: "Roboto", sans-serif; font-size: 8px; font-weight: 500; color: #fff; }
  .preview-banner { left: 0; top: 801px; width: 782px; height: 130px; overflow: hidden;
    background:
      radial-gradient(ellipse 60px 50px at 570px 10px, rgba(150,150,150,.3), rgba(150,150,150,0) 100%),
      linear-gradient(180deg, rgba(185,185,185,0) 60%, rgba(185,185,185,.35) 80%, rgba(215,215,215,.2) 100%),
      linear-gradient(90deg, #e9e9e9 0%, #ececec 40%, #e3e3e3 75%, #d6d6d6 100%); }
  .channel-bar { left: 0; top: 931px; width: 782px; height: 60px; background: var(--bar-dark); border-bottom: 1px solid #444; }
  .avatar { position: absolute; left: 124px; top: 7px; width: 33px; height: 33px; border-radius: 50%; background: #fff; }
  .channel-name { position: absolute; left: 167px; top: 11px; font-family: "Roboto", sans-serif; font-size: 9.5px; color: #fff; }
  .channel-subs { position: absolute; left: 167px; top: 25px; font-family: "Roboto", sans-serif; font-size: 5px; color: var(--muted); }
  .subscribe { position: absolute; left: 583px; top: 16px; width: 76px; height: 14px; background: var(--subscribe);
    color: #fff; font-family: "Roboto", sans-serif; font-size: 5.5px; font-weight: 500; display: flex; align-items: center; justify-content: center; }
  .tabs { position: absolute; left: 124px; top: 45px; display: flex; font-family: "Roboto", sans-serif; font-size: 5.2px; color: var(--muted); }
  .tabs span { width: 52px; text-align: center; padding-bottom: 7px; }
  .tabs .active { color: #fff; border-bottom: 1.5px solid #bbb; }

  /* Closing */
  .closing { left: 288px; top: 1020px; z-index: 0; isolation: isolate;
    font-family: "Montserrat", sans-serif; font-weight: 900; font-size: 60px; line-height: 54px; letter-spacing: -3px; color: var(--ink); }
  .closing .you { position: relative; display: inline-block; }
  .closing .you::before { content: ""; position: absolute; left: 8px; width: 82px; top: 27px; height: 24px; background: var(--brand-red); z-index: -1; }
</style>
</head>
<body>

  <section class="abs logo-light">
    <div class="wordmark wordmark--lg wordmark--red" style="left:118px; top:108px"><span class="dot"></span>Cozy Nook Attic Sound</div>
  </section>
  <section class="abs logo-dark">
    <div class="wordmark wordmark--lg wordmark--white" style="left:118px; top:108px"><span class="dot"></span>Cozy Nook Attic Sound</div>
  </section>
  <div class="section-title section-title--on-light" style="top:13px">THE <span class="underline">LO</span>GO</div>
  <div class="section-title section-title--on-dark" aria-hidden="true" style="top:13px">THE <span class="underline">LO</span>GO</div>

  <div class="section-title" style="top:271px">THE <span class="underline">BAN</span>NER</div>
  <section class="abs banner" role="img" aria-label="Banner: softly faded photo of a home recording studio with monitors and mixing desk, and a circular pattern of instrument and headphone icons on the left">
    <div class="banner-pattern"></div>
    <div class="wordmark wordmark--md wordmark--red" style="left:328px; top:198px"><span class="dot"></span>Cozy Nook Attic Sound</div>
    <div class="tagline" style="left:492px; top:196px">
      <h2>A regular Joe blowin’<br>his dough on gear<br>and guitars</h2>
      <p>Follow my Studio Renovation | Free How-To’s</p>
    </div>
    <div class="contact" style="left:326px; top:277px"><span class="icon"><svg width="5" height="4" viewBox="0 0 5 4"><rect x=".3" y=".3" width="4.4" height="3.4" fill="none" stroke="#fff" stroke-width=".6"/><path d="M.3 .3 2.5 2 4.7 .3" fill="none" stroke="#fff" stroke-width=".6"/></svg></span>hello@cozynookattic.net</div>
  </section>

  <div class="section-title" style="top:747px">A <span class="underline">PREV</span>IEW</div>
  <header class="abs topbar">
    <svg class="abs" style="left:124px; top:8px" width="8" height="7" viewBox="0 0 8 7"><path d="M0 .5h8M0 3.5h8M0 6.5h8" stroke="#fff" stroke-width="1"/></svg>
    <span class="site-name">Vidora</span>
    <div class="search"></div>
    <div class="search-btn"></div>
    <svg class="abs" style="left:603px; top:7px" width="60" height="10" viewBox="0 0 60 10">
      <path d="M5 1 2 4h2v3h2V4h2zM1.5 9h7" stroke="#aaa" stroke-width=".8" fill="#aaa"/>
      <path d="M22 2c2 0 3 1.5 3 3.5V7h1v1h-8V7h1V5.5C19 3.5 20 2 22 2z" fill="#aaa"/>
      <circle cx="46" cy="5" r="4.5" fill="none" stroke="#888" stroke-width="1"/>
    </svg>
  </header>
  <section class="abs preview-banner" role="img" aria-label="Channel banner shown inside the channel page layout">
    <div class="banner-pattern" style="top:-200px"></div>
    <div class="wordmark wordmark--md wordmark--red" style="left:328px; top:34px"><span class="dot"></span>Cozy Nook Attic Sound</div>
    <div class="tagline" style="left:492px; top:30px">
      <h2>A regular Joe blowin’<br>his dough on gear<br>and guitars</h2>
      <p>Follow my Studio Renovation | Free How-To’s</p>
    </div>
    <div class="contact" style="left:326px; top:109px"><span class="icon"><svg width="5" height="4" viewBox="0 0 5 4"><rect x=".3" y=".3" width="4.4" height="3.4" fill="none" stroke="#fff" stroke-width=".6"/><path d="M.3 .3 2.5 2 4.7 .3" fill="none" stroke="#fff" stroke-width=".6"/></svg></span>hello@cozynookattic.net</div>
  </section>
  <section class="abs channel-bar">
    <div class="avatar"></div>
    <div class="channel-name">Cozy Nook Attic Sound</div>
    <div class="channel-subs">500.000 subscribers</div>
    <div class="subscribe">SUBSCRIBE</div>
    <nav class="tabs">
      <span class="active">HOME</span><span>VIDEOS</span><span>PLAYLISTS</span><span>CHANNELS</span><span>DISCUSSION</span><span>ABOUT</span>
      <span><svg width="7" height="7" viewBox="0 0 7 7"><circle cx="3" cy="3" r="2.2" fill="none" stroke="#999" stroke-width=".8"/><path d="M4.6 4.6 6.6 6.6" stroke="#999" stroke-width=".8"/></svg></span>
    </nav>
  </section>

  <div class="abs closing">THANK<br><span class="you">YOU</span></div>

</body>
</html>
```